CalmHarbor Homepage and Landing Pages

Please see detailed brief.

CalmHarbor is Australia’s newest online therapy and mental health service. We allow patients from across australia to connect with Mental health practitioners from across Australia. Our mission is to remove the friction in gaining support for mental health related issues.

Number of Pages Required

1 page

Font styles to use
Sans Serif

Colors
33a6d7
0293ce
3277b5
0255a3
acd136
9bcb3c

Requirements
Must have
• Please see detailed brief.
Nice to have
• Please see detailed brief
Should not have

```html
<!DOCTYPE html>
<html lang="en">
<head>
<meta charset="utf-8">
<title>CalmHarbor — Online Therapy</title>
<link href="https://fonts.googleapis.com/css2?family=Karla:wght@400;500;700&family=Roboto:wght@400;500;700&display=swap" rel="stylesheet">
<style>
  :root {
    --brand: #0aa8f8;
    --brand-deep: #0255a3;
    --brand-mid: #3277b5;
    --ink: #111111;
    --body: #333333;
    --nav: #3a3a3a;
    --white: #ffffff;
    --illo-light: #33a6d7;
  }
  * { box-sizing: border-box; margin: 0; padding: 0; }
  html, body { width: 1200px; height: 2644px; overflow: hidden; background: var(--white); }
  .page { position: relative; width: 1200px; height: 2644px; font-family: "Karla", sans-serif; color: var(--body); }
  .abs { position: absolute; }

  /* header */
  .brand { display: flex; align-items: center; gap: 10px; font-family: "Karla", sans-serif; font-size: 31px; font-weight: 400; color: var(--nav); }
  .brand-dot { width: 22px; height: 22px; border-radius: 50%; background: var(--brand); }
  .site-logo { left: 56px; top: 52px; }
  .main-nav { left: 389px; top: 66px; display: flex; gap: 26px; font-family: "Roboto", sans-serif; font-weight: 500; font-size: 14.5px; letter-spacing: 0.4px; color: var(--nav); }
  .login-btn { left: 976px; top: 51px; width: 172px; height: 48px; border-radius: 24px; background: var(--brand); color: var(--white); font-family: "Roboto", sans-serif; font-weight: 500; font-size: 13.5px; display: flex; align-items: center; justify-content: center; gap: 8px; }
  .login-btn svg { width: 20px; height: 20px; }

  /* buttons */
  .pill { display: flex; align-items: center; justify-content: center; gap: 10px; border-radius: 22px; font-family: "Roboto", sans-serif; font-weight: 500; font-size: 16px; letter-spacing: 0.5px; }
  .pill svg { width: 16px; height: 14px; }
  .pill-solid { background: var(--brand); color: var(--white); }
  .pill-light { background: var(--white); color: var(--brand); }

  h1, h2 { font-family: "Roboto", sans-serif; font-weight: 700; }

  /* hero */
  .hero-title { left: 89px; top: 248px; font-size: 41px; line-height: 48px; color: var(--ink); letter-spacing: -0.3px; }
  .hero-copy { left: 89px; top: 356px; width: 370px; font-size: 20.5px; line-height: 34px; letter-spacing: 0.3px; }
  .hero-cta { left: 90px; top: 520px; width: 156px; height: 43px; }
  .hero-art { left: 621px; top: 246px; width: 468px; height: 314px; border-radius: 140px 160px 40px 40px; background: linear-gradient(135deg, var(--brand) 0%, #0a6fd8 55%, var(--brand-deep) 100%); }

  /* mission band */
  .mission-band { left: 0; top: 775px; width: 1200px; height: 676px; background: var(--brand); }
  .mission-title { left: 157px; top: 936px; font-size: 41px; line-height: 47px; color: var(--white); }
  .mission-copy { left: 157px; top: 1045px; width: 370px; font-size: 20.5px; line-height: 34px; letter-spacing: 0.3px; color: var(--white); }
  .mission-cta { left: 158px; top: 1209px; width: 191px; height: 43px; }
  .mission-circle { left: 601px; top: 854px; width: 518px; height: 518px; border-radius: 50%; background: var(--white); }
  .app-shot { left: 750px; top: 947px; width: 220px; height: 321px; background: linear-gradient(160deg, #2b2b2b 0%, #6f6a62 45%, #d8dde3 100%); }
  .circle-caption { left: 601px; top: 1300px; width: 518px; text-align: center; font-family: "Roboto", sans-serif; font-weight: 500; font-size: 15.5px; letter-spacing: 0.6px; color: var(--ink); }

  /* find help */
  .profile-shot { left: 202px; top: 1623px; width: 229px; height: 435px; background: linear-gradient(180deg, #1e1e1e 0%, #f2f4f6 20%, #e8ecef 80%, #1e1e1e 100%); }
  .find-title { left: 556px; top: 1703px; font-size: 41px; line-height: 48px; color: var(--ink); letter-spacing: -0.3px; }
  .find-copy { left: 558px; top: 1774px; width: 500px; font-size: 20.5px; line-height: 34px; letter-spacing: 0.3px; }
  .find-cta { left: 558px; top: 1938px; width: 247px; height: 43px; }

  /* footer */
  .site-footer { left: 0; top: 2241px; width: 1200px; height: 330px; background: var(--brand); }
  .footer-logo { left: 90px; top: 2288px; width: 216px; height: 59px; background: var(--white); padding-left: 12px; }
  .footer-logo .brand { height: 59px; font-size: 30px; }
  .footer-blurb { left: 90px; top: 2357px; width: 232px; font-size: 11px; line-height: 13.5px; color: var(--white); }
  .contact-list { left: 90px; top: 2412px; list-style: none; font-family: "Roboto", sans-serif; font-weight: 500; font-size: 14px; line-height: 23px; letter-spacing: 0.8px; color: var(--white); }
  .support-title { left: 419px; top: 2294px; font-family: "Roboto", sans-serif; font-weight: 500; font-size: 16px; letter-spacing: 1px; color: var(--white); }
  .support-rule { left: 419px; top: 2321px; width: 178px; height: 3px; background: var(--white); }
  .support-links { left: 418px; top: 2334px; list-style: none; font-family: "Roboto", sans-serif; font-weight: 500; font-size: 14px; line-height: 23px; letter-spacing: 0.9px; color: var(--white); }
  .social-row { left: 418px; top: 2480px; display: flex; gap: 8px; }
  .social-row span { width: 22px; height: 22px; border: 2px solid var(--white); border-radius: 4px; }
  .question-title { left: 717px; top: 2294px; font-family: "Roboto", sans-serif; font-weight: 500; font-size: 23px; letter-spacing: 0.8px; color: var(--white); }
  .field { background: var(--white); font-size: 11px; color: #888; padding: 11px 13px; letter-spacing: 0.4px; }
  .field-name { left: 718px; top: 2339px; width: 190px; height: 39px; padding-top: 14px; }
  .field-email { left: 922px; top: 2339px; width: 189px; height: 39px; }
  .field-message { left: 718px; top: 2390px; width: 393px; height: 99px; }
  .submit-btn { left: 987px; top: 2505px; width: 124px; height: 38px; border: 1.5px solid var(--white); color: var(--white); font-family: "Roboto", sans-serif; font-weight: 700; font-size: 11px; letter-spacing: 1.5px; display: flex; align-items: center; justify-content: center; gap: 6px; }
  .copyright { left: 0; top: 2598px; width: 1200px; text-align: center; font-family: "Karla", sans-serif; font-size: 13.5px; letter-spacing: 2px; color: #222; }
</style>
</head>
<body>
<div class="page">

  <header>
    <div class="abs site-logo brand"><span class="brand-dot"></span>CalmHarbor</div>
    <nav class="abs main-nav">
      <span>FOR PRACTITIONERS</span>
      <span>HOW IT WORKS?</span>
      <span>MEET OUR TEAM</span>
      <span>CONTACT</span>
    </nav>
    <div class="abs login-btn">
      <svg viewBox="0 0 20 20" fill="none" stroke="#fff" stroke-width="1.6"><circle cx="10" cy="10" r="8.5"/><circle cx="10" cy="8" r="3"/><path d="M5 15.5c1.5-2.5 8.5-2.5 10 0"/></svg>
      PATIENT LOG IN
    </div>
  </header>

  <section class="hero">
    <h1 class="abs hero-title">Book Online Appointment<br>in minutes, 24/7</h1>
    <p class="abs hero-copy">CalmHarbor provides on-demand access to a range of psychologists &amp; personal wellness professionals from across Australia.</p>
    <div class="abs pill pill-solid hero-cta">BOOK NOW
      <svg viewBox="0 0 16 14" fill="none" stroke="#fff" stroke-width="2.2"><path d="M1 7h13M8.5 1.5 14 7l-5.5 5.5"/></svg>
    </div>
    <div class="abs hero-art" role="img" aria-label="Illustration of two practitioners assembling puzzle pieces shaped like a human head"></div>
  </section>

  <section>
    <div class="abs mission-band"></div>
    <h2 class="abs mission-title">Our Mission<br>is Simple</h2>
    <p class="abs mission-copy">We want to break down the barriers in receiving effective treatment and care for anxiety, stress and mental health related issues.</p>
    <div class="abs pill pill-light mission-cta">HOW IT WORKS
      <svg viewBox="0 0 16 14" fill="none" stroke="#0aa8f8" stroke-width="2.2"><path d="M1 7h13M8.5 1.5 14 7l-5.5 5.5"/></svg>
    </div>
    <div class="abs mission-circle"></div>
    <div class="abs app-shot" role="img" aria-label="App screens showing a video consultation and a date and time booking calendar"></div>
    <div class="abs circle-caption">DUMMY TEXT</div>
  </section>

  <section>
    <div class="abs profile-shot" role="img" aria-label="Phone screen showing a practitioner profile with experience, availability and a Book Now button"></div>
    <h2 class="abs find-title">Find the help you need..</h2>
    <p class="abs find-copy">Book an appointment with one of our highly qualified, licensed practitioners. The consultation can be conducted from wherever you feel most comfortable.&nbsp; No travel. No Clinics.</p>
    <div class="abs pill pill-solid find-cta">FIND A PRACTITIONER
      <svg viewBox="0 0 16 14" fill="none" stroke="#fff" stroke-width="2.2"><path d="M1 7h13M8.5 1.5 14 7l-5.5 5.5"/></svg>
    </div>
  </section>

  <footer>
    <div class="abs site-footer"></div>
    <div class="abs footer-logo"><div class="brand"><span class="brand-dot"></span>CalmHarbor</div></div>
    <p class="abs footer-blurb">Lorem ipsum dolor sit amet consectetur adipiscing elit, Lorem ipsum dolor sit amet, consectetur adipiscing elit</p>
    <ul class="abs contact-list">
      <li>HELLO@CALMHARBOR.COM</li>
      <li>ADDR1 LINE........</li>
      <li>ADDR2 LINE..........</li>
      <li>ADDR3 LINE...........</li>
      <li>+1 (555) 010 - 2468</li>
    </ul>
    <div class="abs support-title">SUPPORT</div>
    <div class="abs support-rule"></div>
    <ul class="abs support-links">
      <li>HELP CENTER</li>
      <li>CONTACT US</li>
      <li>ABOUT US</li>
      <li>CAREERS</li>
      <li>SUBSCRIBE</li>
      <li>BLOG</li>
    </ul>
    <div class="abs social-row" aria-label="Social links"><span></span><span></span><span></span></div>
    <div class="abs question-title">HAVE A QUESTION ?</div>
    <div class="abs field field-name">Name</div>
    <div class="abs field field-email">Email Address</div>
    <div class="abs field field-message">Message</div>
    <div class="abs submit-btn">SUBMIT
      <svg width="6" height="10" viewBox="0 0 6 10" fill="none" stroke="#fff" stroke-width="1.2"><path d="M1 1l4 4-4 4"/></svg>
    </div>
    <div class="abs copyright">©2020 CALMHARBOR INC. ALL RIGHTS RESERVED</div>
  </footer>

</div>
</body>
</html>
```